Veridan Support Coordination

My new business involves providing support coordination for QLPC participants that live with a primary psychosocial and/or developmental delay disability, including but not limited to:

- Anxiety
- Depression
- Bipolar
- Borderline Personality Disorder
- Schizophrenia
- Psychosis
- Autisim Spectrum Disorder
- Fetal Alcohol Spectrum Disorder
- Cerebral Palsy
- Intellectual Disability
- Acquired Brain Injury
- Down Syndrome
- Spina Bifida

The following is an example of another company
https://tallowmerebrook.com/

The are basically 3 types of support we offer
- psychosocial recovery coaching
- support coordination
- specialist support coordination

I have attached a copy of my logo, please utilise this colour scheme for website and business cards.

Target Market(s)

See above

Industry/Entity Type

Health Service

Number of Pages Required

5+ page

Font styles to use
Other font styles liked:
• Arial

Colors

Designer to choose only greyscale colors for use in the design.

```html
<!DOCTYPE html>
<html lang="en">
<head>
<meta charset="utf-8">
<title>Veridan Support Coordination – Planning &amp; Plan Reviews</title>
<link rel="stylesheet" href="https://fonts.googleapis.com/css2?family=Arimo:wght@400;700&family=Questrial&display=swap">
<style>
  :root {
    --brand-blue: #0a8fd6;
    --brand-blue-soft: #a9daf2;
    --brand-green: #7ab929;
    --white: #ffffff;
    --photo-deep: #5e2a45;
    --photo-warm: #8a5a48;
    --photo-denim: #6f86a3;
  }
  * { margin: 0; padding: 0; box-sizing: border-box; }
  html, body {
    width: 1200px; height: 750px; overflow: hidden;
    background: var(--white);
  }
  .page {
    position: relative; width: 1200px; height: 750px; overflow: hidden;
    font-family: "Arimo", Arial, sans-serif; color: var(--brand-blue);
  }

  /* Header */
  .brand {
    position: absolute; left: 20px; top: 10px; width: 130px;
    display: flex; flex-direction: column; align-items: center;
  }
  .brand-mark {
    width: 46px; height: 46px; border-radius: 50%;
    border: 2px solid var(--brand-blue);
  }
  .brand-name {
    margin-top: 6px; font-size: 14px; line-height: 16px; text-align: center;
    color: var(--brand-blue); font-weight: 400;
  }
  .main-nav {
    position: absolute; top: 20px; left: 0; width: 1200px; height: 30px;
  }
  .main-nav a {
    position: absolute; font-size: 24px; color: var(--brand-blue);
    text-decoration: none; white-space: nowrap;
  }
  .nav-rule {
    position: absolute; left: 179px; top: 79px; width: 979px; height: 1px;
    background: var(--brand-blue);
  }

  /* Hero copy */
  .hero-title {
    position: absolute; left: 75px; top: 198px;
    font-family: "Questrial", Arial, sans-serif; font-weight: 400;
    font-size: 56px; line-height: 55px;
    color: transparent; -webkit-text-stroke: 1.3px var(--brand-blue);
  }
  .hero-title span {
    display: inline-block; position: relative;
  }
  .hero-title span::before {
    content: ""; position: absolute; left: 2px; right: 0; bottom: 9px; height: 14px;
    background: var(--brand-blue-soft); z-index: -1;
  }
  .hero-lead {
    position: absolute; left: 73px; top: 340px; width: 560px;
    font-weight: 700; font-size: 27.5px; line-height: 29.5px;
  }
  .hero-body {
    position: absolute; left: 74px; top: 459px; width: 520px;
    font-size: 18.5px; line-height: 20px;
  }
  .more-link {
    position: absolute; left: 74px; top: 572px;
    display: flex; align-items: center; gap: 10px;
    color: var(--brand-green); font-size: 19px; text-decoration: none;
  }
  .more-link .label { text-decoration: underline; text-underline-offset: 2px; }

  /* Hero visual */
  .hero-rings { position: absolute; left: 0; top: 0; }
  .question-bubble {
    position: absolute; left: 1046px; top: 608px; width: 116px; height: 116px;
    border-radius: 50%; background: var(--brand-blue); color: var(--white);
    display: flex; align-items: center; justify-content: center; text-align: center;
    font-size: 18.5px; line-height: 24px;
  }
</style>
</head>
<body>
<div class="page">

  <header>
    <div class="brand">
      <div class="brand-mark"></div>
      <div class="brand-name">Veridan<br>Support Coordination</div>
    </div>
    <nav class="main-nav">
      <a style="left:226px">Home</a>
      <a style="left:344px">QLPC Support</a>
      <a style="left:509px">Our Services</a>
      <a style="left:689px">Planning</a>
      <a style="left:845px">About Us</a>
      <a style="left:1013px">Contact</a>
    </nav>
    <div class="nav-rule"></div>
  </header>

  <svg class="hero-rings" width="1200" height="750" viewBox="0 0 1200 750">
    <defs>
      <linearGradient id="photoTone" x1="0" y1="0" x2="0.4" y2="1">
        <stop offset="0" stop-color="var(--photo-warm)"/>
        <stop offset="0.45" stop-color="var(--photo-deep)"/>
        <stop offset="1" stop-color="var(--photo-denim)"/>
      </linearGradient>
    </defs>
    <g fill="none" stroke="var(--brand-blue)">
      <path d="M832 179 A331 331 0 0 0 861 822" stroke-width="2.5"/>
      <path d="M1047 689 A256 256 0 1 1 1152 384" stroke-width="3"/>
      <path d="M719 508 A205 205 0 0 0 937 691" stroke-width="1"/>
      <path d="M1150 397 A247 247 0 0 1 1135 612" stroke-width="1"/>
      <path d="M737 704 A275 275 0 0 0 1074 717" stroke-width="1"/>
      <path d="M655 480 A266 266 0 0 0 675 605" stroke-width="1"/>
    </g>
    <circle cx="921" cy="489" r="185" fill="url(#photoTone)" stroke="var(--brand-blue)" stroke-width="5"
            role="img" aria-label="Photo of a smiling young man in a wheelchair raising a glass in a toast with friends"/>
  </svg>

  <h1 class="hero-title"><span>Planning &amp; Plan</span><br><span>Reviews</span></h1>

  <p class="hero-lead">Lorem ipsum dolor sit amet, consectetuer ipsum dolor sit amet, consectetuer adipiscing elit, sed</p>

  <p class="hero-body">Qutem vel eum iriure dolor in hendrerit in vulputate velit esse molestie consequat, vel illum dolore eu feugiat, Lorem m, quis nostrud exerci tation ullamcorper suscipit lobortis nisl ut aliquip ex ea commodo</p>

  <a class="more-link" href="#">
    <svg width="24" height="12" viewBox="0 0 24 12" aria-hidden="true">
      <line x1="0" y1="6" x2="16" y2="6" stroke="var(--brand-green)" stroke-width="2.5"/>
      <path d="M13 1 L24 6 L13 11 Z" fill="var(--brand-green)"/>
    </svg>
    <span class="label">More information</span>
  </a>

  <div class="question-bubble">Have a<br>Question?</div>

</div>
</body>
</html>
```